Business Process / Lifecycle Diagram for Consulting Firm

We are a Delaware-based business modernization and transition-readiness firm. We need a clean, professional process diagram that visually represents our client lifecycle. This is not a marketing funnel or sales graphic — it is a product and delivery lifecycle.

The diagram must be reusable across pitch decks, one-pagers, grant applications, and our website.

Required Structure (must follow exactly)
Stage 1 — Diagnose
Enterprise Renewal Audit (ERA)
Shift Preparedness Index™ (SPI)
(Parallel entry points, equal visual weight)

→ Output: Diagnostic Insight & Priority Signals

Stage 2 — Clarify
Modernization Roadmap (Co-Created)

Stage 3 — Modernize
Y2 — Yield & Output Track

Stage 4 — Sustain
Ongoing Modernization Support

Foundation Layer (supports all stages)
TPG-OS™ pillars: People, Process, Systems, Insight

End Outcome
- Operational Clarity
- Sustainable Profitability
- Long-Term Stability

Design Requirements
- Professional, calm (not startup / SaaS style)
- Minimal text, clear hierarchy
- Horizontal or left-to-right flow preferred
- No funnels, no sales language, no aggressive arrows
- Must be delivered as editable vector (AI, SVG, or Figma)

Brand Notes
- Neutral color palette that complements logo attached (Gold Color Code C39E11, Navy Blue code 002C55)
- One accent color for emphasis
- Clean typography
- Should feel credible to business owners, advisors, and lenders
- See website (https://www.tallmerepinesgroup.com/) and LinkedIn (https://www.tallmerepinesgroup.com/) for additional insight into branding.

What NOT to Do
- Do not rename stages
- Do not combine stages
- Do not add extra steps

```html
<!DOCTYPE html>
<html lang="en">
<head>
<meta charset="utf-8">
<title>Tallmere Pines Group — Client Lifecycle</title>
<link rel="stylesheet" href="https://fonts.googleapis.com/css2?family=Montserrat:wght@400;500;600;700;800;900&display=swap">
<style>
  :root{
    --gold:#c39e11;
    --gold-muted:#a3883b;
    --navy:#002c55;
    --navy-mid:#003473;
    --navy-deep:#1a2440;
    --sky:#cfe3f5;
    --sky-soft:#e6f0fa;
    --ink:#333a44;
    --grey:#555b63;
    --paper:#ffffff;
  }
  html,body{margin:0;padding:0;width:1200px;height:1200px;overflow:hidden;background:var(--paper);}
  .lifecycle{display:block;width:1200px;height:1200px;font-family:"Montserrat",sans-serif;}
  .brand-name{font-weight:600;font-size:34px;fill:var(--navy);letter-spacing:1px;}
  .banner-text{font-weight:800;font-size:20px;fill:#fff;letter-spacing:.5px;}
  .stage-kicker{font-weight:800;font-size:11px;fill:var(--gold);letter-spacing:7px;}
  .stage-num{font-weight:900;font-size:36px;fill:var(--navy);}
  .stage-name{font-weight:800;font-size:18px;fill:var(--navy);}
  .detail{font-weight:500;font-size:9.5px;fill:var(--ink);}
  .bullet{fill:var(--gold);}
  .track{stroke:var(--navy);stroke-width:3;stroke-dasharray:2 3;fill:none;}
  .halo{stroke:var(--navy-deep);stroke-width:1.2;stroke-dasharray:3 3;fill:none;}
  .stem{stroke:var(--navy-deep);stroke-width:1.2;stroke-dasharray:3 3;}
  .node{fill:var(--gold);}
  .glyph{stroke:#fff;stroke-width:2.2;fill:none;stroke-linecap:round;stroke-linejoin:round;}
  .ring{fill:#fff;stroke:var(--navy);stroke-width:4;}
  .pillars-label{font-weight:700;font-size:12px;fill:var(--gold);}
  .pillar-text{font-weight:800;font-size:17px;fill:#fff;}
  .foundation-title{font-weight:800;font-size:19px;fill:var(--navy);}
  .foundation-sub{font-weight:400;font-size:11px;fill:var(--grey);}
  .outcome-label{font-weight:600;font-size:14px;fill:var(--grey);}
</style>
</head>
<body>
<svg class="lifecycle" viewBox="0 0 1200 1200" xmlns="http://www.w3.org/2000/svg" role="img" aria-label="Tallmere Pines Group client lifecycle: Diagnose, Clarify, Modernize, Sustain, supported by TPG-OS pillars, leading to three end outcomes">
  <defs>
    <radialGradient id="foundation-glow" cx="50%" cy="50%" r="50%">
      <stop offset="0.55" stop-color="#ffffff"/>
      <stop offset="1" stop-color="#d3e4f6"/>
    </radialGradient>
  </defs>

  <!-- Brand -->
  <g class="brand">
    <text class="brand-name" x="600" y="108" text-anchor="middle">TALLMERE PINES GROUP</text>
  </g>

  <!-- Required structure banner -->
  <g class="banner">
    <rect x="434" y="169" width="334" height="47" rx="4" fill="var(--navy)"/>
    <path d="M591 216 L600 226 L609 216 Z" fill="var(--navy)"/>
    <text class="banner-text" x="601" y="200" text-anchor="middle">REQUIRED STRUCTURE</text>
  </g>

  <!-- Return tracks -->
  <path class="track" d="M1000 406 H1045 Q1105 406 1105 466 V739 Q1105 779 1065 779 H850"/>
  <path class="track" d="M352 779 H170 Q130 779 130 819 V1056 Q130 1096 170 1096 H335"/>
  <path class="track" d="M372 1096 H578"/>
  <path class="track" d="M622 1096 H835"/>

  <!-- Stage connector -->
  <path class="track" d="M251 406 H698"/>
  <path class="track" d="M756 406 H940"/>
  <circle class="ring" cx="349" cy="406" r="9"/>
  <circle class="ring" cx="604" cy="406" r="9"/>
  <circle class="ring" cx="848" cy="406" r="9"/>

  <!-- Stage 01 -->
  <g class="stage">
    <text class="stage-kicker" x="226" y="259" text-anchor="middle">STAGE</text>
    <text class="stage-num" x="222" y="300" text-anchor="middle">01</text>
    <circle cx="222" cy="311" r="3" fill="var(--navy-deep)"/>
    <line class="stem" x1="222" y1="314" x2="222" y2="362"/>
    <path class="halo" d="M186 389 A40 40 0 0 1 258 389"/>
    <circle class="node" cx="222" cy="406" r="29"/>
    <g class="glyph"><circle cx="218" cy="402" r="10"/><line x1="225" y1="409" x2="233" y2="417"/></g>
    <text class="stage-name" x="222" y="462" text-anchor="middle">DIAGNOSE</text>
    <path class="bullet" d="M116 485 l5 3 l-5 3z"/>
    <text class="detail" x="134" y="492">Enterprise Renewal Audit (ERA)</text>
    <path class="bullet" d="M116 514 l5 3 l-5 3z"/>
    <text class="detail" x="134" y="521">Shift Preparedness Index™ (SPI)</text>
    <text class="detail" x="134" y="535">(Parallel entry points, equal visual weight)</text>
  </g>

  <!-- Stage 02 -->
  <g class="stage">
    <text class="stage-kicker" x="490" y="259" text-anchor="middle">STAGE</text>
    <text class="stage-num" x="486" y="300" text-anchor="middle">02</text>
    <circle cx="486" cy="311" r="3" fill="var(--navy-deep)"/>
    <line class="stem" x1="486" y1="314" x2="486" y2="362"/>
    <path class="halo" d="M450 389 A40 40 0 0 1 522 389"/>
    <circle class="node" cx="486" cy="406" r="29"/>
    <g class="glyph">
      <path d="M473 399 v-6 h6 M493 393 h6 v6 M499 413 v6 h-6 M479 419 h-6 v-6"/>
      <rect x="480" y="399" width="12" height="14" stroke-width="1.8"/>
      <line x1="483" y1="404" x2="489" y2="404" stroke-width="1.5"/>
      <line x1="483" y1="408" x2="487" y2="408" stroke-width="1.5"/>
    </g>
    <text class="stage-name" x="486" y="462" text-anchor="middle">CLARIFY</text>
    <path class="bullet" d="M416 485 l5 3 l-5 3z"/>
    <text class="detail" x="434" y="492">Modernization</text>
    <text class="detail" x="434" y="509">Roadmap (Co-Created)</text>
  </g>

  <!-- Stage 03 -->
  <g class="stage">
    <text class="stage-kicker" x="731" y="259" text-anchor="middle">STAGE</text>
    <text class="stage-num" x="727" y="300" text-anchor="middle">03</text>
    <circle cx="727" cy="311" r="3" fill="var(--navy-deep)"/>
    <line class="stem" x1="727" y1="314" x2="727" y2="362"/>
    <path class="halo" d="M691 389 A40 40 0 0 1 763 389"/>
    <circle class="node" cx="727" cy="406" r="29"/>
    <g class="glyph" stroke-width="1.8">
      <path d="M727 392 a14 14 0 1 0 0 28"/>
      <path d="M722 393 l1-5 h4 M716 397 l-4-3 M712 404 l-5 0 M712 409 h-5 M716 416 l-4 3 M722 419 l1 5 h4"/>
      <path d="M727 400 h10 M727 404 h13 M727 408 h15 M727 412 h13 M727 416 h10"/>
      <circle cx="738" cy="400" r="1.5"/><circle cx="742" cy="408" r="1.5"/><circle cx="738" cy="416" r="1.5"/>
    </g>
    <text class="stage-name" x="727" y="462" text-anchor="middle">MODERNIZE</text>
    <path class="bullet" d="M657 485 l5 3 l-5 3z"/>
    <text class="detail" x="673" y="492">Y2 — Yield</text>
    <text class="detail" x="673" y="509">&amp; Output Track</text>
  </g>

  <!-- Stage 04 -->
  <g class="stage">
    <text class="stage-kicker" x="973" y="257" text-anchor="middle">STAGE</text>
    <text class="stage-num" x="969" y="300" text-anchor="middle">04</text>
    <circle cx="969" cy="311" r="3" fill="var(--navy-deep)"/>
    <line class="stem" x1="969" y1="314" x2="969" y2="362"/>
    <path class="halo" d="M933 389 A40 40 0 0 1 1005 389"/>
    <circle class="node" cx="969" cy="406" r="29"/>
    <g class="glyph" stroke-width="1.8">
      <path d="M955 398 a16 16 0 0 1 26 -6"/><path d="M983 414 a16 16 0 0 1 -26 6"/>
      <path d="M978 387 l3 5 l-6 1"/><path d="M960 425 l-3 -5 l6 -1"/>
      <path d="M972 394 l-8 13 h7 l-3 11 l9 -14 h-7 z"/>
    </g>
    <text class="stage-name" x="969" y="462" text-anchor="middle">SUSTAIN</text>
    <path class="bullet" d="M903 485 l5 3 l-5 3z"/>
    <text class="detail" x="919" y="492">Ongoing</text>
    <text class="detail" x="919" y="509">Modernization Support</text>
  </g>

  <!-- Foundation layer -->
  <g class="foundation">
    <ellipse cx="600" cy="765" rx="228" ry="200" fill="url(#foundation-glow)"/>
    <text class="pillars-label" x="600" y="602" text-anchor="middle">TPG-OS™ pillars</text>
    <rect x="487" y="619" width="227" height="303" fill="#fff"/>

    <rect x="492" y="624" width="217" height="68" fill="var(--gold)"/>
    <g class="glyph" stroke-width="1.6">
      <path d="M525 648 a9 9 0 1 1 12 0 v6 h-12 z"/><path d="M526 658 h10 M527 662 h8"/>
      <path d="M531 633 v-4 M519 638 l-3-3 M543 638 l3-3 M515 647 h-4 M547 647 h4"/>
    </g>
    <text class="pillar-text" x="550" y="665">INSIGHT</text>

    <rect x="492" y="699" width="217" height="68" fill="var(--gold-muted)"/>
    <g class="glyph" stroke-width="1.6">
      <circle cx="531" cy="733" r="13" stroke-dasharray="5 2.5"/><circle cx="531" cy="733" r="8"/>
      <path d="M527 733 l3 3 l5 -6"/>
    </g>
    <text class="pillar-text" x="551" y="740">SYSTEMS</text>

    <rect x="492" y="774" width="217" height="68" fill="var(--navy-mid)"/>
    <g class="glyph" stroke-width="1.6">
      <path d="M518 805 a14 14 0 0 1 24 -8"/><path d="M544 812 a14 14 0 0 1 -24 8"/>
      <circle cx="531" cy="808" r="7" stroke-dasharray="3 2"/><circle cx="531" cy="808" r="3"/>
    </g>
    <text class="pillar-text" x="551" y="815">PROCESS</text>

    <rect x="492" y="849" width="217" height="68" fill="var(--navy-deep)"/>
    <g class="glyph" stroke-width="1.6">
      <circle cx="531" cy="874" r="8"/><path d="M516 900 v-4 a10 10 0 0 1 10 -10 h10 a10 10 0 0 1 10 10 v4 z"/>
    </g>
    <text class="pillar-text" x="547" y="890">PEOPLE</text>

    <text class="foundation-title" x="881" y="677" text-anchor="middle">FOUNDATION</text>
    <text class="foundation-title" x="881" y="699" text-anchor="middle">LAYER</text>
    <text class="foundation-sub" x="881" y="724" text-anchor="middle">(SUPPORTS ALL STAGES)</text>
  </g>

  <!-- End outcome banner -->
  <g class="banner">
    <rect x="434" y="988" width="334" height="44" rx="4" fill="var(--navy)"/>
    <path d="M591 1032 L600 1042 L609 1032 Z" fill="var(--navy)"/>
    <text class="banner-text" x="600" y="1017" text-anchor="middle">END OUTCOME</text>
  </g>

  <!-- Outcomes -->
  <g class="outcome">
    <path d="M312 1093 a37 37 0 0 1 74 0 h-12 a25 25 0 0 0 -50 0 z" fill="var(--sky)"/>
    <circle class="node" cx="349" cy="1093" r="19"/>
    <g class="glyph" stroke-width="1.8"><circle cx="349" cy="1093" r="10"/><path d="M344 1093 l4 4 l7 -8"/></g>
    <text class="outcome-label" x="349" y="1141" text-anchor="middle">Operational Clarity</text>
  </g>
  <g class="outcome">
    <path d="M563 1093 a37 37 0 0 1 74 0 h-12 a25 25 0 0 0 -50 0 z" fill="var(--sky)"/>
    <circle class="node" cx="600" cy="1093" r="19"/>
    <g class="glyph" stroke-width="1.8"><circle cx="600" cy="1093" r="10"/><path d="M595 1093 l4 4 l7 -8"/></g>
    <text class="outcome-label" x="600" y="1141" text-anchor="middle">Sustainable Profitability</text>
  </g>
  <g class="outcome">
    <path d="M820 1093 a37 37 0 0 1 74 0 h-12 a25 25 0 0 0 -50 0 z" fill="var(--sky)"/>
    <circle class="node" cx="857" cy="1093" r="19"/>
    <g class="glyph" stroke-width="1.8"><circle cx="857" cy="1093" r="10"/><path d="M852 1093 l4 4 l7 -8"/></g>
    <text class="outcome-label" x="857" y="1141" text-anchor="middle">Long-Term Stability</text>
  </g>
</svg>
</body>
</html>
```